A WEBSITE FOR A JEWELLERY RETAIL STORE WITH A SHOPPING CART, AND ABILITY TO ORDER ONLINE.

I require a website with a shopping cart.

We sell MAINLY diamond jewellery (such as rings etc). I need it to be simple to change prices with only a few buttons, as the price fluctuates due to the US Dollar.

We are a diamond wholesaler, selling directly to the public, so we guarantee the lowest prices in Australia.

There is also a link to current inventory that will need to be uploaded to the site.

This could be an ongoing job, where you will be paid weekly to maintain and update the website if you wish.

Target Market(s)

People getting engaged, and wanting to buy a diamond ring.

Number of Pages Required

5+ page

Colors

Designer to choose colors to be used in the design.

Requirements
Must have
• elegant.
• modern.
• professional.
• SHOPPING CART.
• ABILITY TO SEARCH FOR LOOSE DIAMONDS (LINK THAT NEEDS TO BE EMBEDDED WILL BE SENT WHICH SHOWS CURRENT STOCK).
• ENGAGEMENT RINGS
• WEDDING RINGS
• DIAMOND EARRINGS
• DIAMOND PENDANTS
• LOOSE DIAMONDS.
• SALE ITEMS.
• OTHER JEWELLERY.
• EDUCATION
• WISH LIST
• CART.
Nice to have
• a good place to look for inspiration on pages is https://www.lumenvael.example.
• YOU MAY VISIT OUR FACEBOOK PAGE AT.
• HTTP://WWW.SOCIALPAGE.EXAMPLE/QUILLSTONEJEWELLERS
Should not have
• We don't want it too busy.

```html
<!DOCTYPE html>
<html lang="en">
<head>
<meta charset="utf-8">
<title>Quillstone Jewellers – Wedding Rings</title>
<link href="https://fonts.googleapis.com/css2?family=Montserrat:wght@400;500;600&display=swap" rel="stylesheet">
<style>
:root{
  --ink:#000;
  --paper:#fff;
  --line:#dcdcdc;
  --muted:#222;
  --footer:#141414;
  --footer-text:#f2f2f2;
}
*{box-sizing:border-box;margin:0;padding:0}
html,body{width:690px;height:1200px;overflow:hidden;background:var(--paper)}
body{position:relative;font-family:'Montserrat',sans-serif;color:var(--ink)}
.topbar{position:absolute;left:0;top:0;width:690px;height:14px;background:var(--ink);color:var(--paper);font-size:6px}
.topbar-item{position:absolute;top:3px;display:flex;align-items:center;gap:5px}
.topbar-item svg{width:8px;height:8px}
.site-header{position:absolute;left:0;top:14px;width:690px;height:40px;background:var(--paper);border-bottom:1px solid var(--line)}
.brand{position:absolute;left:70px;top:13px;display:flex;align-items:center;gap:5px;font-size:10px;font-weight:500;letter-spacing:.5px;color:var(--ink);white-space:nowrap}
.brand-mark{width:12px;height:12px;background:var(--ink);flex:none}
.main-nav a{position:absolute;top:16px;font-size:6px;color:var(--ink);text-decoration:none}
.search{position:absolute;left:519px;top:15px;width:78px;height:11px;border:1px solid var(--ink);display:flex;justify-content:flex-end}
.search span{width:12px;height:100%;background:var(--ink);display:flex;align-items:center;justify-content:center}
.cart{position:absolute;left:610px;top:15px}
.hero{position:absolute;left:0;top:54px;width:690px;height:228px;background:radial-gradient(ellipse at 50% 55%,#c9a25a 0%,#8a7754 22%,#5e5e5e 45%,#8d8d8d 75%,#b6b6b6 100%)}
.category-bar{position:absolute;left:0;top:282px;width:690px;height:21px;background:var(--ink)}
.category-tab{position:absolute;top:0;height:21px;line-height:21px;font-size:7.5px;color:var(--paper);text-decoration:none;transform:translateX(-50%);letter-spacing:.2px;white-space:nowrap}
.category-tab.active{background:var(--paper);color:var(--ink);width:79px;text-align:center;left:87px;transform:none}
.product-grid{position:absolute;left:128px;top:331px;display:grid;grid-template-columns:repeat(3,138px);grid-auto-rows:192px;column-gap:10px;row-gap:8px}
.product-card{position:relative;border:1px solid var(--line);background:var(--paper);text-align:center}
.product-photo{position:absolute;left:33px;top:9px;width:72px;height:72px;border-radius:50%;background:radial-gradient(circle at 50% 40%,#ffffff 0%,#e6e8ec 45%,#c9ccd2 70%,#fff 72%)}
.product-photo.gold{background:radial-gradient(circle at 50% 40%,#ffffff 0%,#e8e8ea 45%,#d8c488 70%,#fff 72%)}
.product-code{position:absolute;left:0;right:0;top:93px;font-size:7.5px;font-weight:400}
.product-desc{position:absolute;left:0;right:0;top:105px;font-size:5px;line-height:7px}
.product-price{position:absolute;left:0;right:0;top:124px;font-size:10px}
.btn{display:inline-block;background:var(--ink);color:var(--paper);font-size:5px;height:11px;line-height:11px;width:54px;text-align:center}
.product-actions{position:absolute;left:0;right:0;top:151px;display:flex;justify-content:center;gap:4px}
.product-details{position:absolute;left:0;right:0;top:168px;display:flex;justify-content:center}
.pagination{position:absolute;left:289px;top:954px;display:flex;align-items:center;font-size:6px}
.page{width:13px;height:12px;line-height:12px;text-align:center}
.page.current{background:var(--ink);color:var(--paper);margin-right:4px}
.page-next{margin-left:6px;width:54px;height:12px;line-height:12px;background:var(--ink);color:var(--paper);text-align:center}
.site-footer{position:absolute;left:0;top:999px;width:690px;height:175px;background:var(--footer);color:var(--footer-text)}
.footer-brand{position:absolute;left:134px;top:28px;display:flex;align-items:center;gap:4px;font-size:7.5px;font-weight:500;letter-spacing:.3px;white-space:nowrap}
.footer-brand .brand-mark{width:10px;height:10px;background:var(--footer-text)}
.contact{position:absolute;left:134px;top:60px;font-size:5.5px;line-height:7px}
.contact p{margin-bottom:6px}
.hours{display:grid;grid-template-columns:52px auto;row-gap:1.5px}
.footer-heading{position:absolute;top:27px;font-size:9px;font-weight:600}
.footer-links{position:absolute;left:295px;top:60px;list-style:none;font-size:5.5px;line-height:8.6px}
.enquiry{position:absolute;left:421px;top:51px;width:136px}
.field{height:11px;background:var(--paper);margin-bottom:3px;font-size:5px;color:#bbb;padding:2px 7px}
.field.message{height:42px}
.send{margin-top:4px;height:11px;border:1px solid var(--footer-text);text-align:center;font-size:5.5px;line-height:10px}
.copyright{position:absolute;left:0;top:1174px;width:690px;height:26px;line-height:26px;text-align:center;font-size:7px}
</style>
</head>
<body>
<div class="topbar">
  <div class="topbar-item" style="left:430px">
    <svg viewBox="0 0 10 10"><circle cx="5" cy="5" r="5" fill="#fff"/><path d="M3.3 2.6l1 1-.5.7c.4.8 1 1.4 1.8 1.8l.7-.5 1 1-.7.9C4.8 7.3 2.7 5.2 2.4 3.3z" fill="#000"/></svg>
    +61 400 555 012
  </div>
  <div class="topbar-item" style="left:519px">
    <svg viewBox="0 0 10 10"><circle cx="5" cy="5" r="5" fill="#fff"/><rect x="2.5" y="3.3" width="5" height="3.4" fill="#000"/><path d="M2.5 3.3L5 5.2 7.5 3.3" stroke="#fff" stroke-width=".5" fill="none"/></svg>
    sales@quillstonejewellers.example
  </div>
</div>

<header class="site-header">
  <div class="brand"><span class="brand-mark"></span>QUILLSTONE JEWELLERS</div>
  <nav class="main-nav">
    <a href="#" style="left:258px">Home</a>
    <a href="#" style="left:293px">Shop</a>
    <a href="#" style="left:325px">Loose Diamonds</a>
    <a href="#" style="left:390px">Contact Us</a>
    <a href="#" style="left:439px">Education</a>
    <a href="#" style="left:486px">Wish List</a>
  </nav>
  <div class="search"><span><svg width="7" height="7" viewBox="0 0 10 10"><circle cx="4" cy="4" r="3" stroke="#fff" stroke-width="1.4" fill="none"/><path d="M6.2 6.2L9 9" stroke="#fff" stroke-width="1.6"/></svg></span></div>
  <svg class="cart" width="10" height="9" viewBox="0 0 12 11"><path d="M0 1h2l1.5 6h6L11 3H3" stroke="#000" stroke-width="1.3" fill="none"/><circle cx="4.5" cy="9.5" r="1" fill="#000"/><circle cx="8.5" cy="9.5" r="1" fill="#000"/><circle cx="11" cy="1.2" r="1.2" fill="#d40000"/></svg>
</header>

<div class="hero" role="img" aria-label="Close-up of three stacked gold diamond rings on a grey stone surface"></div>

<nav class="category-bar">
  <a href="#" class="category-tab active">-Wedding Rings</a>
  <a href="#" class="category-tab" style="left:213px">-Diamond Earrings</a>
  <a href="#" class="category-tab" style="left:305px">-Engagement Rings</a>
  <a href="#" class="category-tab" style="left:400px">-Diamond Pendants</a>
  <a href="#" class="category-tab" style="left:490px">-Loose Diamonds</a>
  <a href="#" class="category-tab" style="left:573px">-Other Jewellery</a>
</nav>

<main class="product-grid">
  <article class="product-card"><div class="product-photo gold" role="img" aria-label="Yellow gold cushion halo diamond ring"></div><h3 class="product-code">R-1652</h3><p class="product-desc">1.5CT MARQUISE HALO.<br>1.20CT CENTRE. D SI2.</p><p class="product-price">$2500</p><div class="product-actions"><span class="btn">Add to Cart</span><span class="btn">Wishlist</span></div><div class="product-details"><span class="btn">Details</span></div></article>
  <article class="product-card"><div class="product-photo" role="img" aria-label="White gold marquise halo diamond ring"></div><h3 class="product-code">R-1361</h3><p class="product-desc">1.5CT MARQUISE HALO.<br>1.20CT CENTRE. D SI2.</p><p class="product-price">$3000</p><div class="product-actions"><span class="btn">Add to Cart</span><span class="btn">Wishlist</span></div><div class="product-details"><span class="btn">Details</span></div></article>
  <article class="product-card"><div class="product-photo" role="img" aria-label="White gold split-shank round diamond ring"></div><h3 class="product-code">R-1444</h3><p class="product-desc">1.5CT MARQUISE HALO.<br>1.20CT CENTRE. D SI2.</p><p class="product-price">$3500</p><div class="product-actions"><span class="btn">Add to Cart</span><span class="btn">Wishlist</span></div><div class="product-details"><span class="btn">Details</span></div></article>
  <article class="product-card"><div class="product-photo gold" role="img" aria-label="Yellow gold cushion halo diamond ring"></div><h3 class="product-code">R-1652</h3><p class="product-desc">1.5CT MARQUISE HALO.<br>1.20CT CENTRE. D SI2.</p><p class="product-price">$2500</p><div class="product-actions"><span class="btn">Add to Cart</span><span class="btn">Wishlist</span></div><div class="product-details"><span class="btn">Details</span></div></article>
  <article class="product-card"><div class="product-photo" role="img" aria-label="White gold marquise halo diamond ring"></div><h3 class="product-code">R-1361</h3><p class="product-desc">1.5CT MARQUISE HALO.<br>1.20CT CENTRE. D SI2.</p><p class="product-price">$3000</p><div class="product-actions"><span class="btn">Add to Cart</span><span class="btn">Wishlist</span></div><div class="product-details"><span class="btn">Details</span></div></article>
  <article class="product-card"><div class="product-photo" role="img" aria-label="White gold split-shank round diamond ring"></div><h3 class="product-code">R-1444</h3><p class="product-desc">1.5CT MARQUISE HALO.<br>1.20CT CENTRE. D SI2.</p><p class="product-price">$3500</p><div class="product-actions"><span class="btn">Add to Cart</span><span class="btn">Wishlist</span></div><div class="product-details"><span class="btn">Details</span></div></article>
  <article class="product-card"><div class="product-photo gold" role="img" aria-label="Yellow gold cushion halo diamond ring"></div><h3 class="product-code">R-1652</h3><p class="product-desc">1.5CT MARQUISE HALO.<br>1.20CT CENTRE. D SI2.</p><p class="product-price">$2500</p><div class="product-actions"><span class="btn">Add to Cart</span><span class="btn">Wishlist</span></div><div class="product-details"><span class="btn">Details</span></div></article>
  <article class="product-card"><div class="product-photo" role="img" aria-label="White gold marquise halo diamond ring"></div><h3 class="product-code">R-1361</h3><p class="product-desc">1.5CT MARQUISE HALO.<br>1.20CT CENTRE. D SI2.</p><p class="product-price">$3000</p><div class="product-actions"><span class="btn">Add to Cart</span><span class="btn">Wishlist</span></div><div class="product-details"><span class="btn">Details</span></div></article>
  <article class="product-card"><div class="product-photo" role="img" aria-label="White gold split-shank round diamond ring"></div><h3 class="product-code">R-1444</h3><p class="product-desc">1.5CT MARQUISE HALO.<br>1.20CT CENTRE. D SI2.</p><p class="product-price">$3500</p><div class="product-actions"><span class="btn">Add to Cart</span><span class="btn">Wishlist</span></div><div class="product-details"><span class="btn">Details</span></div></article>
</main>

<nav class="pagination">
  <span class="page current">1</span><span class="page">2</span><span class="page">3</span><span class="page">4</span><span class="page-next">Next</span>
</nav>

<footer class="site-footer">
  <div class="footer-brand"><span class="brand-mark"></span>QUILLSTONE JEWELLERS</div>
  <div class="contact">
    <p>Harbourgate Shopping Centre<br>Elmsford, Victoria, Australia</p>
    <p>Call: +61 400 555 012</p>
    <p>Email: sales@quillstonejewellers.example</p>
    <div class="hours">
      <span>Mon - Wed</span><span>9:00 am - 5:30 pm</span>
      <span>Thu - Fri</span><span>9:00 am - 9:00 pm</span>
      <span>Sat</span><span>9:00 am - 5:00 pm</span>
      <span>Sun</span><span>10:00 am - 5:00 pm</span>
    </div>
  </div>
  <h4 class="footer-heading" style="left:295px">Products</h4>
  <ul class="footer-links">
    <li>Wedding Rings</li><li>Engagement Rings</li><li>Diamond Earrings</li><li>Diamond Pendants</li><li>Loose Diamonds</li><li>Sales Items</li><li>Other Jewellery</li>
  </ul>
  <h4 class="footer-heading" style="left:420px">We're Here to Help!</h4>
  <form class="enquiry">
    <div class="field">Name</div>
    <div class="field">Email</div>
    <div class="field message">Message</div>
    <div class="send">Send</div>
  </form>
</footer>

<div class="copyright">Copyright © 2017 Quillstone Jewellers - All Rights Reserved.</div>
</body>
</html>
```